BRM Going Cashless

Hello,
We are a medical office looking to get a flyer created to promote to our patients we will be going "Cashless." Our tagline will be "Cash-Less is Stress-Less"

"Starting in July, to offer you the fastest and most convenient service, we are transitioning to a cashless system. You can now enjoy faster checkout times and greater security with card and contactless payments. More info to come."

I've added two other flyers as sample designs we've used.

Please include logo, addresses, website, phone number

Files to include jpeg, png, pdf (under 5mb), Facebook and Instagram sizing.

Thank you,
Marlo

```html
<!DOCTYPE html>
<html lang="en">
<head>
<meta charset="utf-8">
<title>Brightmoor Foot &amp; Ankle – Cash-Less is Stress-Less</title>
<link rel="stylesheet" href="https://fonts.googleapis.com/css2?family=Poppins:wght@400;500;600;700;800&family=Sacramento&display=swap">
<style>
  :root{
    --page:#f3f3f3;
    --dark:#2b2b2b;
    --ring:#363636;
    --teal:#4fc1a6;
    --orange:#f27d42;
    --paper:#e3e3e3;
    --ink:#333333;
    --white:#ffffff;
  }
  *{box-sizing:border-box;margin:0;padding:0}
  html,body{width:1200px;height:1200px;overflow:hidden;background:var(--page);font-family:"Poppins",sans-serif}
  .canvas{position:relative;width:1200px;height:1200px}

  .flyer{position:absolute;background:var(--dark);overflow:hidden}
  .flyer--portrait{left:50px;top:227px;width:582px;height:748px}
  .flyer--square{left:673px;top:358px;width:486px;height:486px}

  .flyer > *{position:absolute}
  .rings{left:0;top:0;width:100%;height:100%}

  .brand{display:flex;align-items:center;gap:8px;color:var(--orange);font-weight:700;line-height:1.05;text-transform:uppercase}
  .brand__dot{border-radius:50%;background:var(--teal);flex:none}
  .flyer--portrait .brand{left:188px;top:16px;font-size:21px}
  .flyer--portrait .brand__dot{width:46px;height:46px}
  .flyer--square .brand{left:164px;top:8px;font-size:16px}
  .flyer--square .brand__dot{width:36px;height:36px}

  .headline{left:0;width:100%;text-align:center;font-weight:800;letter-spacing:-0.5px;line-height:1}
  .headline span{display:block}
  .headline__cash{color:var(--teal)}
  .headline__stress{color:var(--orange)}
  .flyer--portrait .headline{top:112px;font-size:80px;padding-left:8px}
  .flyer--portrait .headline span + span{margin-top:-4px}
  .flyer--square .headline{top:68px;font-size:50px;padding-left:8px}
  .flyer--square .headline span + span{margin-top:-3px}

  .connector{font-family:"Sacramento",cursive;color:var(--white);line-height:1;transform:rotate(-8deg)}
  .flyer--portrait .connector{left:236px;top:146px;font-size:96px}
  .flyer--square .connector{left:220px;top:96px;font-size:60px}

  .intro{color:var(--white);text-align:justify;font-weight:400}
  .flyer--portrait .intro{left:29px;top:310px;width:268px;font-size:17px;line-height:24px}
  .flyer--square .intro{left:28px;top:190px;width:226px;font-size:12.3px;line-height:18.5px}

  .terminal{border-radius:26px;background:linear-gradient(160deg,#f1f1f1 0%,#b9bcc0 45%,#3a3d42 100%)}
  .flyer--portrait .terminal{left:322px;top:292px;width:236px;height:288px;transform:rotate(-12deg)}
  .flyer--square .terminal{left:293px;top:178px;width:156px;height:190px;transform:rotate(-12deg)}

  .tear{left:0;width:100%}
  .flyer--portrait .tear{top:520px;height:228px}
  .flyer--square .tear{top:320px;height:166px}

  .phone{display:flex;align-items:center;color:var(--ink);font-weight:600;letter-spacing:0.5px}
  .phone__icon{flex:none}
  .flyer--portrait .phone{left:20px;top:563px;font-size:31px;gap:10px}
  .flyer--portrait .phone__icon{width:36px;height:36px}
  .flyer--square .phone{left:16px;top:360px;font-size:24px;gap:8px}
  .flyer--square .phone__icon{width:28px;height:28px}

  .web{left:0;background:var(--teal);color:var(--dark);border-radius:0 999px 999px 0;display:flex;align-items:center;font-weight:400}
  .web b{font-weight:700}
  .flyer--portrait .web{top:609px;width:315px;height:33px;font-size:24px;padding-left:20px}
  .flyer--square .web{top:393px;width:251px;height:27px;font-size:19px;padding-left:19px}

  .offices{left:0;width:100%;display:grid;grid-template-columns:repeat(3,1fr);color:var(--ink);text-align:center}
  .office__name{font-weight:600;display:flex;align-items:center;justify-content:center;gap:6px}
  .office__pin{flex:none}
  .office__line{font-weight:400}
  .flyer--portrait .offices{top:654px;padding:0 8px}
  .flyer--portrait .office__name{font-size:14.5px;margin-bottom:4px}
  .flyer--portrait .office__pin{width:14px;height:16px}
  .flyer--portrait .office__line{font-size:13px;line-height:18.5px}
  .flyer--square .offices{top:428px;padding:0 4px}
  .flyer--square .office__name{font-size:11.3px;margin-bottom:2px}
  .flyer--square .office__pin{width:10px;height:12px}
  .flyer--square .office__line{font-size:10px;line-height:13.5px}
</style>
</head>
<body>
<main class="canvas">

  <!-- Portrait flyer -->
  <section class="flyer flyer--portrait">
    <svg class="rings" viewBox="0 0 582 748" aria-hidden="true">
      <circle cx="292" cy="140" r="240" fill="none" stroke="var(--ring)" stroke-width="60"/>
    </svg>

    <div class="brand"><span class="brand__dot"></span><span>Brightmoor<br>Foot &amp; Ankle</span></div>

    <h1 class="headline"><span class="headline__cash">Cash-Less</span><span class="headline__stress">Stress-Less</span></h1>
    <span class="connector">is</span>

    <p class="intro">Starting in July, to offer you the fastest and most convenient service, we are transitioning to a cashless system. You can now enjoy faster checkout times and greater security with card and contactless payments. More info to come.</p>

    <svg class="tear" viewBox="0 0 582 228" preserveAspectRatio="none" aria-hidden="true">
      <polygon fill="var(--white)" points="0,18 30,14 60,8 90,12 120,4 150,10 180,2 210,8 240,4 270,16 300,28 330,34 360,42 400,52 440,58 470,46 500,34 540,40 582,30 582,228 0,228"/>
      <polygon fill="var(--paper)" points="0,26 35,22 62,16 92,20 122,12 152,18 182,10 212,16 242,12 272,24 302,36 332,42 362,50 402,60 442,66 472,54 502,42 542,48 582,38 582,228 0,228"/>
    </svg>

    <div class="terminal" role="img" aria-label="Photo of a card payment terminal with a receipt roll and an inserted credit card"></div>

    <div class="phone">
      <svg class="phone__icon" viewBox="0 0 36 36" aria-hidden="true">
        <circle cx="18" cy="18" r="16.5" fill="none" stroke="var(--orange)" stroke-width="2"/>
        <path d="M12 10c1-1 2-1 3 0l2 3c.6 1 .3 1.8-.5 2.4l-1 .8c.8 2 2.4 3.6 4.3 4.4l.8-1c.6-.8 1.5-1.1 2.4-.5l3 2c1 .7 1 2 0 3l-1.3 1.3c-1.2 1.2-3.2 1.3-5.4.2-3.5-1.8-6.4-4.7-8.2-8.2-1.1-2.2-1-4.2.2-5.4z" fill="var(--orange)"/>
      </svg>
      <span>(555)014-0192</span>
    </div>

    <div class="web">www.<b>stepwellfeet</b>.com</div>

    <div class="offices">
      <div class="office">
        <div class="office__name"><svg class="office__pin" viewBox="0 0 14 16" aria-hidden="true"><path d="M7 1a5 5 0 0 1 5 5c0 3-5 8-5 8S2 9 2 6a5 5 0 0 1 5-5z" fill="none" stroke="var(--orange)" stroke-width="1.6"/><circle cx="7" cy="6" r="1.8" fill="var(--orange)"/></svg>Northgate Office</div>
        <div class="office__line">88 Linden Park Dr.</div>
        <div class="office__line">Ste. 120</div>
        <div class="office__line">Northgate, MD 20614</div>
      </div>
      <div class="office">
        <div class="office__name"><svg class="office__pin" viewBox="0 0 14 16" aria-hidden="true"><path d="M7 1a5 5 0 0 1 5 5c0 3-5 8-5 8S2 9 2 6a5 5 0 0 1 5-5z" fill="none" stroke="var(--orange)" stroke-width="1.6"/><circle cx="7" cy="6" r="1.8" fill="var(--orange)"/></svg>Riverside Office</div>
        <div class="office__line">2210 Alder Grove Blvd.</div>
        <div class="office__line">Ste. 305</div>
        <div class="office__line">Riverside, MD 20617</div>
      </div>
      <div class="office">
        <div class="office__name"><svg class="office__pin" viewBox="0 0 14 16" aria-hidden="true"><path d="M7 1a5 5 0 0 1 5 5c0 3-5 8-5 8S2 9 2 6a5 5 0 0 1 5-5z" fill="none" stroke="var(--orange)" stroke-width="1.6"/><circle cx="7" cy="6" r="1.8" fill="var(--orange)"/></svg>Hillcrest Office</div>
        <div class="office__line">47 Wellness Way</div>
        <div class="office__line">Hillcrest, WV 26880</div>
      </div>
    </div>
  </section>

  <!-- Square flyer -->
  <section class="flyer flyer--square">
    <svg class="rings" viewBox="0 0 486 486" aria-hidden="true">
      <circle cx="243" cy="105" r="180" fill="none" stroke="var(--ring)" stroke-width="50"/>
    </svg>

    <div class="brand"><span class="brand__dot"></span><span>Brightmoor<br>Foot &amp; Ankle</span></div>

    <h2 class="headline"><span class="headline__cash">Cash-Less</span><span class="headline__stress">Stress-Less</span></h2>
    <span class="connector">is</span>

    <p class="intro">Starting in July, to offer you the fastest and most convenient service, we are transitioning to a cashless system. You can now enjoy faster checkout times and greater security with card and contactless payments. More info to come.</p>

    <svg class="tear" viewBox="0 0 486 166" preserveAspectRatio="none" aria-hidden="true">
      <polygon fill="var(--white)" points="0,14 30,10 60,6 90,10 120,4 150,8 180,2 210,10 240,20 270,30 300,44 330,56 360,60 390,52 420,40 450,36 486,28 486,166 0,166"/>
      <polygon fill="var(--paper)" points="0,22 32,18 62,14 92,18 122,12 152,16 182,10 212,18 242,28 272,38 302,52 332,64 362,68 392,60 422,48 452,44 486,36 486,166 0,166"/>
    </svg>

    <div class="terminal" role="img" aria-label="Photo of a card payment terminal with a receipt roll and an inserted credit card"></div>

    <div class="phone">
      <svg class="phone__icon" viewBox="0 0 36 36" aria-hidden="true">
        <circle cx="18" cy="18" r="16.5" fill="none" stroke="var(--orange)" stroke-width="2"/>
        <path d="M12 10c1-1 2-1 3 0l2 3c.6 1 .3 1.8-.5 2.4l-1 .8c.8 2 2.4 3.6 4.3 4.4l.8-1c.6-.8 1.5-1.1 2.4-.5l3 2c1 .7 1 2 0 3l-1.3 1.3c-1.2 1.2-3.2 1.3-5.4.2-3.5-1.8-6.4-4.7-8.2-8.2-1.1-2.2-1-4.2.2-5.4z" fill="var(--orange)"/>
      </svg>
      <span>(555)014-0192</span>
    </div>

    <div class="web">www.<b>stepwellfeet</b>.com</div>

    <div class="offices">
      <div class="office">
        <div class="office__name"><svg class="office__pin" viewBox="0 0 14 16" aria-hidden="true"><path d="M7 1a5 5 0 0 1 5 5c0 3-5 8-5 8S2 9 2 6a5 5 0 0 1 5-5z" fill="none" stroke="var(--orange)" stroke-width="1.6"/><circle cx="7" cy="6" r="1.8" fill="var(--orange)"/></svg>Northgate Office</div>
        <div class="office__line">88 Linden Park Dr.</div>
        <div class="office__line">Ste. 120</div>
        <div class="office__line">Northgate, MD 20614</div>
      </div>
      <div class="office">
        <div class="office__name"><svg class="office__pin" viewBox="0 0 14 16" aria-hidden="true"><path d="M7 1a5 5 0 0 1 5 5c0 3-5 8-5 8S2 9 2 6a5 5 0 0 1 5-5z" fill="none" stroke="var(--orange)" stroke-width="1.6"/><circle cx="7" cy="6" r="1.8" fill="var(--orange)"/></svg>Riverside Office</div>
        <div class="office__line">2210 Alder Grove Blvd.</div>
        <div class="office__line">Ste. 305</div>
        <div class="office__line">Riverside, MD 20617</div>
      </div>
      <div class="office">
        <div class="office__name"><svg class="office__pin" viewBox="0 0 14 16" aria-hidden="true"><path d="M7 1a5 5 0 0 1 5 5c0 3-5 8-5 8S2 9 2 6a5 5 0 0 1 5-5z" fill="none" stroke="var(--orange)" stroke-width="1.6"/><circle cx="7" cy="6" r="1.8" fill="var(--orange)"/></svg>Hillcrest Office</div>
        <div class="office__line">47 Wellness Way</div>
        <div class="office__line">Hillcrest, WV 26880</div>
      </div>
    </div>
  </section>

</main>
</body>
</html>
```